Velmora health leaflet

We are looking for a new brand identity for our clinic to start with a new leaflet for communication. For current brand identity please look at our website Www.velmorahealth.cz. We would like to use less of the blue but more of the green turquoise and white. The logo should remain. See attached. We received few ideas but not sure about them. The design should be elegant and simple. Premium
#729694 Hex Color Code
The hexadecimal color code #729694 is a shade of cyan. In the RGB color model #729694 is composed of 44.71% red, 58.82% green and 58.04% blue. In the HSL color space #729694 has a hue of 177° (degrees), 15% saturation and 52% lightness. This color has an approximate wavelength of 492.66 nm.
Main headlines
Playfair Display
Serif, elegant
Body & UI
Lato
Clean, modern
Look and feel
Each slider illustrates characteristics of the customer's brand and the style your logo design should communicate.

```html
<!DOCTYPE html>
<html lang="en">
<head>
<meta charset="UTF-8">
<title>Velmora health leaflet</title>
<link rel="stylesheet" href="https://fonts.googleapis.com/css2?family=Playfair+Display:wght@400;500&family=Lato:wght@400;700&family=Merriweather:wght@300;400&display=swap">
<style>
  :root {
    --teal: #4b8e8b;
    --teal-dark: #3f7d7a;
    --teal-soft: #729694;
    --white: #ffffff;
    --paper: #fafafa;
    --ink: #3d4446;
    --ink-soft: #6b7375;
    --backdrop: #efefef;
    --rule: #d9dede;
  }
  * { box-sizing: border-box; margin: 0; padding: 0; }
  html, body { width: 1200px; height: 610px; overflow: hidden; }
  body {
    background: var(--backdrop);
    font-family: "Lato", sans-serif;
    color: var(--ink);
    position: relative;
  }
  .panel {
    position: absolute;
    top: 117px;
    width: 200px;
    height: 413px;
    overflow: hidden;
  }
  .panel--cover { left: 174px; background: var(--teal); color: var(--white); }
  .panel--story { left: 394px; width: 193px; background: var(--white); }
  .panel--services { left: 606px; width: 193px; background: var(--paper); }
  .panel--contact { left: 819px; width: 203px; background: var(--teal); color: var(--white); }

  /* Cover */
  .cover-rule { position: absolute; left: 19px; width: 1px; background: rgba(255,255,255,0.45); }
  .cover-rule--top { top: 0; height: 218px; }
  .cover-rule--bottom { top: 331px; height: 70px; }
  .cover-side-note {
    position: absolute; left: 15px; top: 240px; width: 8px; height: 76px;
    writing-mode: vertical-rl; transform: rotate(180deg);
    font-size: 4.5px; letter-spacing: 0.12em; text-transform: uppercase;
    color: rgba(255,255,255,0.55); white-space: nowrap;
  }
  .cover-headline {
    position: absolute; right: 12px; top: 32px; width: 180px;
    font-family: "Merriweather", "Playfair Display", serif; font-weight: 300;
    font-size: 28px; line-height: 34px; text-align: right;
  }
  .cover-tagline {
    position: absolute; left: 44px; top: 290px; width: 140px;
    font-family: "Merriweather", serif; font-weight: 300;
    font-size: 10px; line-height: 13.5px; text-align: center; opacity: 0.95;
  }
  .brand-foot {
    position: absolute; bottom: 24px; left: 0; right: 0; text-align: center;
    font-size: 7px; letter-spacing: 0.08em; text-transform: uppercase;
  }
  .brand-foot strong { font-weight: 700; }
  .panel--cover .brand-foot { color: rgba(255,255,255,0.8); }
  .panel--story .brand-foot { color: var(--ink); }

  /* Story */
  .story-photo {
    position: absolute; left: 0; top: 0; width: 193px; height: 413px;
    background: linear-gradient(90deg, #8f9394 0%, #c9cbcb 22%, #ececec 42%, #ffffff 60%);
  }
  .story-rule { position: absolute; left: 176px; top: 0; height: 413px; width: 1px; background: var(--rule); }
  .feature-list { position: absolute; left: 16px; top: 72px; width: 156px; list-style: none; }
  .feature-list li {
    position: relative; padding-left: 14px; margin-bottom: 12px;
    font-size: 6px; line-height: 8.5px; color: var(--ink);
  }
  .bullet {
    position: absolute; left: 0; top: 0; width: 9px; height: 9px;
    border-radius: 50%; background: var(--teal);
  }
  .bullet svg { display: block; width: 9px; height: 9px; }

  /* Services */
  .services-head {
    position: absolute; left: 0; top: 0; width: 193px; height: 76px;
    background: var(--white); border-bottom: 1px solid var(--rule);
  }
  .partner-name {
    position: absolute; right: 12px; top: 11px;
    font-family: "Lato", sans-serif; font-weight: 400; font-size: 7.5px;
    color: var(--ink-soft);
  }
  .services-intro {
    position: absolute; left: 22px; top: 50px; width: 156px;
    font-size: 6px; line-height: 8.5px; color: var(--ink);
  }
  .services-body { position: absolute; left: 12px; top: 96px; width: 170px; }
  .services-body p { font-size: 5.6px; line-height: 8px; color: var(--ink-soft); margin: 0 0 10px 10px; }
  .services-body ul { list-style: none; margin-bottom: 10px; }
  .services-body li {
    position: relative; padding-left: 14px; margin-bottom: 7px;
    font-size: 5.6px; line-height: 8px; color: var(--ink);
  }

  /* Contact */
  .building-photo {
    position: absolute; left: 0; top: 0; width: 203px; height: 156px;
    background: linear-gradient(180deg, #8fb6d6 0%, #b8cfdf 40%, #8a9ea9 75%, #5f7a6c 100%);
  }
  .contact-name {
    position: absolute; left: 0; right: 0; top: 202px; text-align: center;
    font-family: "Playfair Display", serif; font-size: 18px; font-weight: 400;
  }
  .contact-grid {
    position: absolute; left: 18px; top: 255px; width: 172px;
    display: grid; grid-template-columns: 1fr 1fr; row-gap: 18px;
    font-size: 5.6px; line-height: 8px; color: rgba(255,255,255,0.9);
  }
  .contact-grid h3 { font-size: 6.2px; font-weight: 700; letter-spacing: 0.04em; text-transform: uppercase; color: var(--white); }
  .contact-grid .center { text-align: center; }
  .contact-url {
    position: absolute; bottom: 24px; left: 0; right: 0; text-align: center;
    font-size: 7px; letter-spacing: 0.06em; text-transform: uppercase; color: rgba(255,255,255,0.8);
  }
</style>
</head>
<body>

<section class="panel panel--cover">
  <span class="cover-rule cover-rule--top"></span>
  <span class="cover-side-note">Velmora health longevity</span>
  <span class="cover-rule cover-rule--bottom"></span>
  <h1 class="cover-headline">Add Healthy<br>Years to<br>Your<br>Life</h1>
  <p class="cover-tagline">Europe's first center of excellence in medicine &amp; healthy longevity.</p>
  <p class="brand-foot">Velmora <strong>Health</strong></p>
</section>

<section class="panel panel--story">
  <div class="story-photo" role="img" aria-label="Soft black and white portrait photograph fading to white"></div>
  <span class="story-rule"></span>
  <ul class="feature-list">
    <li><span class="bullet"><svg viewBox="0 0 9 9"><path d="M2.5 4.6l1.4 1.4 2.6-2.8" fill="none" stroke="#fff" stroke-width="0.9"/></svg></span>Each program starts with a thorough health review.</li>
    <li><span class="bullet"><svg viewBox="0 0 9 9"><path d="M2.5 4.6l1.4 1.4 2.6-2.8" fill="none" stroke="#fff" stroke-width="0.9"/></svg></span>Longevity care shaped by the latest research, with a plan made for your goals and your daily life.</li>
    <li><span class="bullet"><svg viewBox="0 0 9 9"><path d="M2.5 4.6l1.4 1.4 2.6-2.8" fill="none" stroke="#fff" stroke-width="0.9"/></svg></span>Diagnostics and early detection carried out by specialists in calm, private rooms.</li>
    <li><span class="bullet"><svg viewBox="0 0 9 9"><path d="M2.5 4.6l1.4 1.4 2.6-2.8" fill="none" stroke="#fff" stroke-width="0.9"/></svg></span>Specialist teams work together on nutrition, sleep, movement and recovery plans.</li>
    <li><span class="bullet"><svg viewBox="0 0 9 9"><path d="M2.5 4.6l1.4 1.4 2.6-2.8" fill="none" stroke="#fff" stroke-width="0.9"/></svg></span>Regular reviews track your progress over time.</li>
    <li><span class="bullet"><svg viewBox="0 0 9 9"><path d="M2.5 4.6l1.4 1.4 2.6-2.8" fill="none" stroke="#fff" stroke-width="0.9"/></svg></span>Direct access to your doctor by phone.</li>
  </ul>
  <p class="brand-foot">Velmora <strong>Health</strong></p>
</section>

<section class="panel panel--services">
  <header class="services-head">
    <span class="partner-name">Aldern Partners</span>
    <p class="services-intro">Every plan is personal. Tailored care for a longer, healthier life.</p>
  </header>
  <div class="services-body">
    <p>We combine modern medicine with preventive care to help you feel well and stay well for years ahead.</p>
    <ul>
      <li><span class="bullet"><svg viewBox="0 0 9 9"><path d="M2.5 4.6l1.4 1.4 2.6-2.8" fill="none" stroke="#fff" stroke-width="0.9"/></svg></span>Personal physician available whenever you need support and advice.</li>
      <li><span class="bullet"><svg viewBox="0 0 9 9"><path d="M2.5 4.6l1.4 1.4 2.6-2.8" fill="none" stroke="#fff" stroke-width="0.9"/></svg></span>Advanced screening and lab tests.</li>
      <li><span class="bullet"><svg viewBox="0 0 9 9"><path d="M2.5 4.6l1.4 1.4 2.6-2.8" fill="none" stroke="#fff" stroke-width="0.9"/></svg></span>Clear reports with practical next steps.</li>
      <li><span class="bullet"><svg viewBox="0 0 9 9"><path d="M2.5 4.6l1.4 1.4 2.6-2.8" fill="none" stroke="#fff" stroke-width="0.9"/></svg></span>Nutrition and fitness guidance from our team.</li>
    </ul>
    <p>Our clinic offers a quiet setting where time with your doctor is never rushed and every question is heard.</p>
    <p>Membership includes ongoing care, follow-up visits and coordinated referrals to trusted partners.</p>
    <ul>
      <li><span class="bullet"><svg viewBox="0 0 9 9"><path d="M2.5 4.6l1.4 1.4 2.6-2.8" fill="none" stroke="#fff" stroke-width="0.9"/></svg></span>Discreet service designed around your schedule and privacy.</li>
    </ul>
  </div>
</section>

<section class="panel panel--contact">
  <div class="building-photo" role="img" aria-label="Photograph of a modern glass clinic building under a blue sky"></div>
  <p class="contact-name">Velmora health</p>
  <div class="contact-grid">
    <div>
      <h3>Consultation hours</h3>
      <p>Mon–Fri 8:00 – 18:00</p>
      <p>info@velmorahealth.cz</p>
    </div>
    <div class="center">
      <p>Phone</p>
      <p>+420 555 010 200</p>
    </div>
    <div class="center">
      <h3>Velmora health</h3>
      <p>Lindenova 1024/5</p>
      <p>140 00 Praha 4</p>
    </div>
    <div class="center">
      <h3>Velmora health</h3>
      <p>Kaštanová 18</p>
      <p>140 00 Praha 4</p>
    </div>
  </div>
  <p class="contact-url">Www.velmorahealth.cz</p>
</section>

</body>
</html>
```